Business Card Design

We need a business card for a new company in Sydney, Australia. The business supports the tourism industry, predominantly in the IT and systems area. The company focus is to assist business' to streamline their systems and processes, making the back end more efficient with the end goal making them more effective and profitable.

We would like a design that uses the colours red, white and possible black.

Target Market(s)

Tourism companies

Industry/Entity Type

Tourism

Contact Information for Business Card

Morna Kelleway
VantaLoop
Tel: (+61) 0438 716 254
Email: Morna@vantaloop.com.au

Requirements
Nice to have
• Top right corner of the card rounded.

```html
<!DOCTYPE html>
<html lang="en">
<head>
<meta charset="utf-8">
<title>Morna Kelleway VantaLoop – Business Card</title>
<link rel="stylesheet" href="https://fonts.googleapis.com/css2?family=Caprasimo&display=swap">
<style>
  :root {
    --card-red: #ff0a00;
    --card-deep-red: #a80700;
    --card-black: #070808;
    --card-white: #ffffff;
    --page-bg: #ffffff;
  }
  html, body {
    margin: 0;
    padding: 0;
    width: 1200px;
    height: 741px;
    overflow: hidden;
    background: var(--page-bg);
  }
  .business-card {
    display: block;
    width: 1200px;
    height: 741px;
  }
  .card-frame { fill: var(--card-white); stroke: var(--card-black); stroke-width: 3; }
  .card-name,
  .card-contact {
    font-family: "Caprasimo", "Cooper Black", serif;
    paint-order: stroke fill;
    stroke-linejoin: round;
  }
  .card-name {
    font-size: 68px;
    letter-spacing: 1px;
    fill: var(--card-white);
    stroke: var(--card-black);
    stroke-width: 9;
  }
  .card-name .company-name {
    fill: var(--card-black);
    stroke: var(--card-white);
  }
  .card-contact {
    font-size: 35px;
    fill: var(--card-white);
    stroke: var(--card-black);
    stroke-width: 7;
  }
</style>
</head>
<body>
<svg class="business-card" viewBox="0 0 1110 685" preserveAspectRatio="none" xmlns="http://www.w3.org/2000/svg">
  <defs>
    <clipPath id="card-shape">
      <path d="M1.5 1.5 H1025 A83 83 0 0 1 1108.5 84.5 V683.5 H1.5 Z"/>
    </clipPath>
    <linearGradient id="artwork-tone" x1="0" y1="0" x2="1" y2="1">
      <stop offset="0" stop-color="var(--card-red)"/>
      <stop offset="0.45" stop-color="var(--card-deep-red)"/>
      <stop offset="0.7" stop-color="var(--card-black)"/>
      <stop offset="1" stop-color="var(--card-red)"/>
    </linearGradient>
  </defs>

  <path class="card-frame" d="M1.5 1.5 H1025 A83 83 0 0 1 1108.5 84.5 V683.5 H1.5 Z"/>

  <g clip-path="url(#card-shape)">
    <rect class="card-artwork" role="img" aria-label="Red, black and white crossing diagonal band artwork"
          x="12" y="12" width="1084" height="661" fill="url(#artwork-tone)"/>
  </g>

  <text class="card-name" x="555" y="298" text-anchor="middle">Morna Kelleway <tspan class="company-name">VantaLoop</tspan></text>

  <text class="card-contact" x="555" y="522" text-anchor="middle">Tel : (+61) 0438 716 254</text>
  <text class="card-contact" x="555" y="576" text-anchor="middle">Email : Morna @ vantaloop.com.au</text>
</svg>
</body>
</html>
```